Need a revamp of our website to attract larger companies and government authorities. The site must breathe that we are a company ready for larger projects both in the web and app sector. And also, that we can start projects with short notice.

Until now the design suggestions for us have been mor suitable for smaller firms but we have now taken the step in the larger/bigger range.

Most of our web nowadays has been work on digitalization of all kinds of administrative systems.

The site to be redone is https://brightquill.eu And that brand is a sub brand to https://tallmoor.se

startpage
servicelist presentation page
service detail page
caselist page (same as article list)
case detail page (same as article detail)
about us page
contact us page
Updates

We have this video that can be used as a hero banner video

https://www.filecrate.example/t/9QpLmZr4TxWbNvKc

Target Market(s)

b2b customers

Coding

Coded - Design and coding required

Number of Pages Required

5+ page

Font styles to use
Sans Serif

Requirements
Must have
• A thought throu theme. with details folowing the whole design www.pexanor.se
Nice to have
• maybe a video hero banner https://www.filecrate.example/t/9QpLmZr4TxWbNvKc
Should not have
• a standard theme look and feel.

```html
<!DOCTYPE html>
<html lang="en">
<head>
<meta charset="utf-8">
<title>Bright Quill – Web &amp; Mobile Apps</title>
<link rel="stylesheet" href="https://fonts.googleapis.com/css2?family=Poppins:wght@500;600;700&family=Roboto:wght@400;500&display=swap">
<style>
:root{
  --navy:#13263a;
  --navy-deep:#0c1b2a;
  --slate:#34505f;
  --slate-soft:#4a6677;
  --mint:#a9d8c9;
  --ink:#1b1b1b;
  --text:#3a3a3a;
  --white:#ffffff;
  --black:#050607;
  --line:#d9e2e6;
}
*{margin:0;padding:0;box-sizing:border-box}
html,body{width:1200px;height:3595px;overflow:hidden;background:var(--white)}
body{position:relative;font-family:"Roboto",sans-serif;color:var(--text)}
.abs{position:absolute}
h1,h2,h3,h4,.btn,.brand{font-family:"Poppins",sans-serif}

/* header */
.topbar{left:0;top:0;width:1200px;height:105px;background:var(--white);z-index:4}
.brand{left:128px;top:10px;width:170px;text-align:center;z-index:6}
.brand-mark{width:46px;height:46px;margin:0 auto 8px;background:var(--navy);border-radius:4px}
.brand-name{font-size:19px;font-weight:500;letter-spacing:1.5px;color:var(--navy)}
.contact-item{top:14px;display:flex;align-items:center;gap:12px;z-index:6}
.contact-item .ico{width:42px;height:42px;border-radius:50%;background:var(--navy);display:flex;align-items:center;justify-content:center}
.contact-item strong{display:block;font-family:"Poppins",sans-serif;font-weight:500;font-size:16px;color:var(--ink)}
.contact-item span{font-size:13px;color:#666}
.login{left:938px;top:14px;width:112px;height:42px;border-radius:21px;background:var(--white);box-shadow:0 2px 10px rgba(0,0,0,.12);display:flex;align-items:center;gap:10px;padding-left:2px;font-family:"Poppins",sans-serif;font-size:16px;color:var(--ink);z-index:6}
.login .ico{width:40px;height:40px;border-radius:50%;background:var(--navy);display:flex;align-items:center;justify-content:center}
.nav{left:318px;top:78px;width:882px;height:54px;background:var(--slate);clip-path:polygon(24px 0,100% 0,100% 100%,0 100%);z-index:5}
.nav ul{list-style:none;display:flex;align-items:center;height:100%;gap:25px;padding-left:53px;font-size:15px;color:var(--white)}

/* hero */
.hero-photo{left:0;top:105px;width:1200px;height:760px;background:linear-gradient(120deg,#5d6b55 0%,#4c5a4a 30%,#6f756b 55%,#3f4a3c 100%)}
.hero-shade{left:0;top:105px;width:1200px;height:760px;background:linear-gradient(90deg,rgba(10,20,30,.55) 0%,rgba(10,20,30,.25) 55%,rgba(10,20,30,.1) 100%)}
.hero-title{left:112px;top:292px;font-size:48px;line-height:60px;font-weight:700;color:var(--white)}
.hero-text{left:114px;top:424px;width:490px;font-size:15.5px;line-height:26px;color:var(--white)}
.btn{display:inline-flex;align-items:center;justify-content:center;height:56px;border-radius:28px;font-size:16px;font-weight:600;color:var(--white)}
.btn-navy{background:var(--navy)}
.btn-slate{background:var(--slate)}
.play{left:853px;top:385px;width:70px;height:70px;border-radius:50%;background:var(--navy);border:4px solid var(--slate-soft);display:flex;align-items:center;justify-content:center}

/* services */
.section-title{width:1200px;left:0;text-align:center;font-size:36px;font-weight:600;color:var(--ink)}
.section-lead{left:250px;width:700px;text-align:center;font-size:15px;line-height:26px}
.service{top:1080px;width:260px;text-align:center}
.service .ring{width:208px;height:208px;margin:0 auto;border-radius:50%;background:var(--navy);display:flex;align-items:center;justify-content:center}
.service .ring-inner{width:184px;height:184px;border-radius:50%;border:3px solid var(--mint);display:flex;align-items:center;justify-content:center}
.service h3{margin-top:20px;font-size:24px;font-weight:600;color:var(--ink)}
.service p{margin:10px auto 0;width:225px;height:72px;overflow:hidden;font-size:14px;line-height:24px}
.service a{display:inline-block;margin-top:12px;font-family:"Poppins",sans-serif;font-weight:600;font-size:16px;color:var(--slate);text-decoration:underline}
.arrow{width:22px;height:22px;border-radius:50%;display:flex;align-items:center;justify-content:center;top:1180px}

/* welcome */
.welcome{left:0;top:1520px;width:1200px;height:489px;background:linear-gradient(90deg,#1b2c3c 0%,#223446 55%,#1a2b3b 100%)}
.welcome-photo{left:555px;top:1478px;width:645px;height:556px;background:linear-gradient(135deg,#7b6a5a 0%,#8d5a2e 50%,#4d3a2a 100%);clip-path:polygon(40% 0,100% 0,100% 53%,62% 100%,0 100%,0 55%,22% 20%)}
.welcome-title{left:114px;top:1590px;font-size:35px;line-height:43px;font-weight:700;color:var(--white)}
.welcome-title span{color:var(--slate-soft)}
.welcome-text{left:114px;top:1700px;width:490px;font-size:15px;line-height:26px;color:var(--white)}

/* clients */
.client-logo{left:153px;width:363px;height:97px;background:var(--white);box-shadow:0 3px 16px rgba(0,0,0,.08);display:flex;align-items:center;justify-content:center;gap:10px;font-family:"Poppins",sans-serif;font-weight:600;font-size:31px;color:#555}
.client-logo.active{border:3px solid var(--mint)}
.client-logo .dot{width:22px;height:22px;border-radius:50%;background:#666}
.case h3{font-size:26px;font-weight:600;color:var(--ink)}
.case h4{margin-top:6px;font-size:19px;font-weight:600;color:var(--slate)}
.case p{margin-top:18px;width:475px;font-size:15px;line-height:26px}

/* quote */
.quote{left:112px;top:2603px;width:976px;height:265px;border-radius:16px;background:linear-gradient(135deg,#36566c 0%,#2b4a5e 50%,#3c5e74 100%);text-align:center;color:var(--white)}
.quote h2{margin-top:36px;font-size:36px;font-weight:500}
.quote p{margin:14px auto 0;width:680px;font-size:13.5px;line-height:26px}

/* footer */
.footer{left:0;top:3069px;width:1200px;height:526px;background:var(--black)}
.f-brand{left:112px;top:3215px;width:250px;text-align:center}
.f-brand .brand-mark{width:66px;height:66px;background:var(--slate-soft)}
.f-brand .brand-name{font-size:30px;color:var(--white);letter-spacing:2px}
.socials{display:flex;justify-content:center;gap:8px;margin-top:24px}
.socials span{width:28px;height:28px;border-radius:50%;background:#2b3a44}
.f-col{top:3225px;color:var(--white)}
.f-col h4{font-size:22px;font-weight:500;margin-bottom:14px}
.f-col ul{list-style:none;font-size:15px;line-height:30px}
.f-col li::before{content:"«";margin-right:8px}
.email-field{width:278px;height:42px;border:1px solid #555;border-radius:4px;padding:0 16px;display:flex;align-items:center;font-size:14px;color:#777}
.subscribe{margin-top:12px;width:278px;height:42px;border-radius:4px;background:var(--slate);display:flex;align-items:center;justify-content:center;font-size:16px;font-weight:500}
.f-rule{left:112px;top:3497px;width:976px;height:1px;background:#222}
.copyright{left:0;top:3535px;width:1200px;text-align:center;font-size:15px;color:var(--white)}
</style>
</head>
<body>

<!-- header -->
<div class="abs topbar"></div>
<div class="abs brand">
  <div class="brand-mark"></div>
  <div class="brand-name">BRIGHT QUILL</div>
</div>
<div class="abs contact-item" style="left:432px">
  <div class="ico"><svg width="18" height="14" viewBox="0 0 18 14"><rect x="0" y="0" width="18" height="14" rx="2" fill="#fff"/><path d="M1 1l8 6 8-6" stroke="#13263a" stroke-width="1.6" fill="none"/></svg></div>
  <div><strong>Send Us Email</strong><span>info@brightquill.eu</span></div>
</div>
<div class="abs contact-item" style="left:685px">
  <div class="ico"><svg width="14" height="18" viewBox="0 0 14 18"><path d="M7 0a7 7 0 0 0-7 7c0 5 7 11 7 11s7-6 7-11a7 7 0 0 0-7-7z" fill="#fff"/><circle cx="7" cy="7" r="2.5" fill="#13263a"/></svg></div>
  <div><strong>Phone</strong><span>+46 (0)40 318 27 90</span></div>
</div>
<div class="abs login">
  <div class="ico"><svg width="16" height="16" viewBox="0 0 16 16"><circle cx="8" cy="4.5" r="4" fill="#fff"/><path d="M0 16c0-5 3.5-7 8-7s8 2 8 7z" fill="#fff"/></svg></div>
  Login
</div>
<nav class="abs nav">
  <ul><li>Start</li><li>Servicelist Presentation</li><li>Service Detail</li><li>Caselist</li><li>Case Detail</li><li>About Us</li><li>Contact Us</li></ul>
</nav>

<!-- hero -->
<div class="abs hero-photo" role="img" aria-label="Hero video still: hands pouring steaming water into a camping mug outdoors"></div>
<div class="abs hero-shade"></div>
<h1 class="abs hero-title">Bright Quill®<br>Web &amp; Mobile Apps</h1>
<p class="abs hero-text">Located in Sweden we have provided software since 1999. With our experts in areas like web development and mobile app development, we provide first-class software and project management.</p>
<div class="abs btn btn-navy" style="left:112px;top:523px;width:173px">Contact Us</div>
<div class="abs btn btn-slate" style="left:301px;top:523px;width:173px">Render Quote</div>
<div class="abs play"><svg width="14" height="16" viewBox="0 0 14 16"><path d="M2 1l11 7-11 7z" fill="#fff"/></svg></div>
<svg class="abs" style="left:0;top:680px" width="1200" height="200" viewBox="0 0 1200 200">
  <path d="M0 95 C300 210 700 100 1200 90 L1200 200 L0 200 Z" fill="#fff"/>
  <path d="M40 80 C320 -10 560 70 790 60 C950 55 1060 90 1168 120 C1060 90 950 72 790 80 C560 90 300 40 40 80 Z" fill="#13263a"/>
  <path d="M185 160 C400 200 620 130 1020 85 C700 150 400 215 185 160 Z" fill="#13263a"/>
</svg>

<!-- services -->
<h2 class="abs section-title" style="top:928px">Some Of Our Services</h2>
<p class="abs section-lead" style="top:984px">Bright Quill® provide senior resources in a vast range of areas within system development. Lately, most of our work has been within the fields of app and web development.</p>
<div class="abs arrow" style="left:112px;background:var(--navy)"><svg width="8" height="10" viewBox="0 0 8 10"><path d="M6 1L2 5l4 4" stroke="#fff" stroke-width="2" fill="none"/></svg></div>
<div class="abs arrow" style="left:1066px;background:var(--mint)"><svg width="8" height="10" viewBox="0 0 8 10"><path d="M2 1l4 4-4 4" stroke="#fff" stroke-width="2" fill="none"/></svg></div>

<div class="abs service" style="left:158px">
  <div class="ring"><div class="ring-inner">
    <svg width="76" height="76" viewBox="0 0 76 76" fill="none" stroke="#fff" stroke-width="2"><rect x="6" y="10" width="64" height="44" rx="3"/><path d="M28 66h20M38 54v12"/><rect x="14" y="18" width="20" height="10"/><path d="M40 20h22M40 26h16M14 36h48M14 44h30"/></svg>
  </div></div>
  <h3>Web Development</h3>
  <p>We provide mainly Corvel CMS based solutions for small or large projects.</p>
  <a>Learn More</a>
</div>
<div class="abs service" style="left:469px">
  <div class="ring"><div class="ring-inner">
    <svg width="76" height="76" viewBox="0 0 76 76" fill="none" stroke="#fff" stroke-width="2"><rect x="14" y="38" width="48" height="28" rx="2"/><path d="M6 70h64"/><circle cx="38" cy="52" r="4"/><path d="M28 22a10 10 0 0 1 20 0v6M26 24v6M50 24v6"/></svg>
  </div></div>
  <h3>Post-Launch Support</h3>
  <p>We offer maintenance for web-sites and mobile apps. After launch, the journey is not over</p>
  <a>Learn More</a>
</div>
<div class="abs service" style="left:780px">
  <div class="ring"><div class="ring-inner">
    <svg width="76" height="76" viewBox="0 0 76 76" fill="none" stroke="#fff" stroke-width="2"><path d="M14 64l6-16 30-30 10 10-30 30z"/><path d="M44 24l10 10"/><circle cx="54" cy="54" r="8"/><circle cx="54" cy="54" r="3"/><circle cx="26" cy="24" r="9"/></svg>
  </div></div>
  <h3>Design and UX</h3>
  <p>Due to our Bright Quill concept we have only the best senior de-signers working for us. That gives</p>
  <a>Learn More</a>
</div>

<!-- welcome -->
<section class="abs welcome"></section>
<div class="abs welcome-photo" role="img" aria-label="Photo of a young developer at a desk, framed in a brand-shaped cutout"></div>
<h2 class="abs welcome-title">WELCOME TO<br><span>BRIGHT QUILL®</span></h2>
<div class="abs welcome-text">
  <p>Bright Quill® is all about creating software smarter by providing a senior expert in each area of the project. With our long experience, we know how to make software better, smarter and faster.</p>
  <p style="margin-top:24px">Give us a call or send a message.</p>
</div>
<div class="abs btn btn-slate" style="left:114px;top:1856px;width:173px">Render Quote</div>

<!-- clients -->
<h2 class="abs section-title" style="top:2108px">Some Of Our Clients</h2>
<div class="abs client-logo active" style="top:2200px"><span class="dot"></span>Fieldwise</div>
<div class="abs client-logo" style="top:2319px">Norvik AB</div>
<div class="abs client-logo" style="top:2439px">Eventia</div>
<div class="abs case" style="left:570px;top:2232px">
  <h3>Service App for farming equipment</h3>
  <h4>Fieldwise AB</h4>
  <p>As far as agricultural machinery is concerned, it is of great impor-tance that maintenance is carried out in accordance with the manu-facturer's recommendations. It affects both the resale value and the operating cost. Bright Quill has been involved from the planning stage and now delivers a complete app linked to business systems and Nimbus ID.</p>
</div>

<!-- quote -->
<section class="abs quote">
  <h2>Bright Quill® Request For Quote</h2>
  <p>Start the exciting journey of creating a mobile app or website by submitting a request for a quote. Requests are handled quickly and with integrity.</p>
</section>
<div class="abs btn btn-navy" style="left:497px;top:2768px;width:173px">Render Quote</div>

<!-- footer -->
<svg class="abs" style="left:0;top:2950px" width="1200" height="160" viewBox="0 0 1200 160">
  <path d="M0 85 C350 60 700 180 1200 75 L1200 160 L0 160 Z" fill="#050607"/>
  <path d="M40 130 C320 40 560 120 790 110 C950 105 1060 70 1168 75 C1060 110 950 125 790 130 C560 140 300 90 40 130 Z" fill="#34505f"/>
  <path d="M185 22 C400 -5 620 60 1020 115 C700 80 400 10 185 22 Z" fill="#13263a"/>
</svg>
<footer class="abs footer"></footer>
<div class="abs f-brand">
  <div class="brand-mark"></div>
  <div class="brand-name">BRIGHT QUILL</div>
  <div class="socials"><span></span><span></span><span></span><span></span></div>
</div>
<div class="abs f-col" style="left:405px">
  <h4>Quick Link</h4>
  <ul><li>Start</li><li>Servicelist Presentation</li><li>Service Detail</li><li>Caselist</li><li>Case Detail</li><li>About Us</li><li>Contact Us</li></ul>
</div>
<div class="abs f-col" style="left:623px">
  <h4>Help Link</h4>
  <ul><li>Terms&amp;conditions</li><li>Privacy Policy</li><li>About Us</li><li>Support</li></ul>
</div>
<div class="abs f-col" style="left:811px">
  <h4>Get Our Newsletter</h4>
  <div class="email-field">Enter Your Email</div>
  <div class="subscribe">Subscribe Now</div>
</div>
<div class="abs f-rule"></div>
<p class="abs copyright">©Copyrights 2022 Bright Quill | &nbsp; All Rights Reserved</p>

</body>
</html>
```